Australian IT Company requires Business Card Design

Bluepeak is an Australian company that specialises in IT consulting & support, software development, project management, network services.

We have been in business for 15 years.

* We require a business card with the following on it:
Logo
Address
Contact Details
Space for staff name, title & mobile number

Industry/Entity Type

Software

```html
<!DOCTYPE html>
<html lang="en">
<head>
<meta charset="utf-8">
<title>Bluepeak Business Card</title>
<link href="https://fonts.googleapis.com/css2?family=Open+Sans:wght@300;400;600;700&display=swap" rel="stylesheet">
<style>
  :root {
    --bg: #e9e6e1;
    --card-white: #fbfbfb;
    --brand-blue: #3f7aa5;
    --brand-blue-dark: #2c5f86;
    --brand-blue-light: #5c9cc4;
    --text-grey: #7b7f84;
    --rule-blue: #4f88b3;
    --square-grey: #a7a9ab;
  }
  * { margin: 0; padding: 0; box-sizing: border-box; }
  html, body { width: 1200px; height: 1023px; overflow: hidden; }
  body {
    background: var(--bg);
    font-family: "Open Sans", Arial, sans-serif;
    position: relative;
  }
  .card {
    position: absolute;
    width: 600px;
    height: 343px;
    border-radius: 3px;
    box-shadow: 0 6px 18px rgba(0,0,0,0.18);
    overflow: hidden;
  }
  .card-front { left: 60px; top: 110px; background: var(--card-white); }
  .card-back {
    left: 540px; top: 570px;
    background: linear-gradient(135deg, var(--brand-blue-dark) 0%, var(--brand-blue-light) 50%, var(--brand-blue) 100%);
  }

  .corner-tab {
    position: absolute; right: 0; top: 0;
    width: 34px; height: 16px;
    background: var(--brand-blue-light);
  }

  .brand { position: absolute; left: 40px; top: 108px; display: flex; align-items: center; gap: 14px; }
  .brand-square { width: 42px; height: 42px; background: var(--brand-blue); }
  .brand-name {
    font-size: 38px; font-weight: 600; letter-spacing: 1px;
    color: var(--brand-blue); line-height: 1;
  }
  .tagline {
    position: absolute; left: 98px; top: 156px;
    font-size: 9.5px; font-weight: 400; letter-spacing: 3.6px;
    color: var(--text-grey); text-transform: uppercase;
    white-space: nowrap;
  }

  .staff { position: absolute; right: 36px; top: 34px; text-align: right; }
  .staff-name { font-size: 21px; font-weight: 700; color: var(--brand-blue); line-height: 1.2; }
  .staff-title { font-size: 13px; color: var(--text-grey); }

  .address {
    position: absolute; right: 36px; top: 100px;
    display: flex; align-items: center; gap: 12px;
  }
  .address-lines { font-size: 13px; line-height: 1.45; color: var(--text-grey); text-align: right; }
  .pin-icon { width: 28px; height: 28px; }

  .divider {
    position: absolute; left: 210px; right: 68px; top: 196px;
    height: 2px; background: var(--rule-blue);
  }
  .divider-tick {
    position: absolute; left: 210px; top: 196px;
    width: 2px; height: 147px; background: var(--rule-blue); opacity: 0.6;
  }

  .contacts {
    position: absolute; left: 226px; top: 222px;
    list-style: none; font-size: 13px; color: var(--text-grey); line-height: 1.9;
  }
  .contacts li { display: flex; align-items: center; gap: 10px; }
  .contact-icon { width: 12px; height: 12px; flex: none; }

  .back-brand {
    position: absolute; left: 50%; top: 50%; transform: translate(-50%, -50%);
    display: flex; align-items: center; gap: 14px;
  }
  .back-brand-square { width: 30px; height: 30px; background: var(--square-grey); }
  .back-brand-name { font-size: 40px; font-weight: 600; letter-spacing: 1px; color: #ffffff; }
</style>
</head>
<body>

<section class="card card-front" aria-label="Business card front">
  <div class="corner-tab"></div>

  <div class="brand">
    <div class="brand-square"></div>
    <span class="brand-name">BLUEPEAK</span>
  </div>
  <div class="tagline">Technology partners you trust</div>

  <div class="staff">
    <div class="staff-name">Daniel Hart</div>
    <div class="staff-title">Director</div>
  </div>

  <div class="address">
    <svg class="pin-icon" viewBox="0 0 28 28" aria-hidden="true">
      <circle cx="14" cy="14" r="12.5" fill="none" stroke="#3f7aa5" stroke-width="1.6"/>
      <path d="M14 7a4.5 4.5 0 0 0-4.5 4.5c0 3.4 4.5 8.5 4.5 8.5s4.5-5.1 4.5-8.5A4.5 4.5 0 0 0 14 7z" fill="#3f7aa5"/>
      <circle cx="14" cy="11.5" r="1.7" fill="#fbfbfb"/>
    </svg>
    <div class="address-lines">
      14 Harbour Lane<br>
      Level 3<br>
      Carlton Vic 3053
    </div>
  </div>

  <div class="divider"></div>
  <div class="divider-tick"></div>

  <ul class="contacts">
    <li>
      <svg class="contact-icon" viewBox="0 0 12 12" aria-hidden="true"><rect width="12" height="12" rx="2" fill="#5c9cc4"/><path d="M3.5 3c.6 2.6 2.4 4.6 5 5.4l.8-1-1.3-.8-.6.6C6.3 6.7 5.4 5.8 4.9 4.7l.6-.6-.8-1.3z" fill="#fff"/></svg>
      +61 3 9555 0142
    </li>
    <li>
      <svg class="contact-icon" viewBox="0 0 12 12" aria-hidden="true"><rect width="12" height="12" rx="2" fill="#5c9cc4"/><rect x="2.5" y="3.5" width="7" height="5" fill="none" stroke="#fff" stroke-width="1"/><path d="M2.5 3.5 6 6.3 9.5 3.5" fill="none" stroke="#fff" stroke-width="1"/></svg>
      (staff members email address)
    </li>
    <li>
      <svg class="contact-icon" viewBox="0 0 12 12" aria-hidden="true"><rect width="12" height="12" rx="2" fill="#5c9cc4"/><circle cx="6" cy="6" r="3.3" fill="none" stroke="#fff" stroke-width="1"/><path d="M2.7 6h6.6M6 2.7v6.6" stroke="#fff" stroke-width="0.8"/></svg>
      www.bluepeak.net.au
    </li>
  </ul>
</section>

<section class="card card-back" aria-label="Business card back">
  <div class="back-brand">
    <div class="back-brand-square"></div>
    <span class="back-brand-name">BLUEPEAK</span>
  </div>
</section>

</body>
</html>
```